Silver Heron Construction Services

Create a business card for my business consulting company
Danielle Vesk, Founder and CEO
4816 Alder Brook Way, Ste 100
Denver, CO. 80451
303.782.4190 cell
dvesk@silverheronconst.example
www.silverheronconst.example

Target Market(s)

Private Equity and Construction Companies

Industry/Entity Type

Business / Sales Consulting

Contact Information for Business Card

Tag Line that says "Where The Road To Success Is Always Under Construction"

Requirements
Must have
• Logo on both sides of the card.
Nice to have
• Add tagline to the same side of the card as my name and contact info

```html
<!DOCTYPE html>
<html lang="en">
<head>
<meta charset="utf-8">
<title>Silver Heron Construction Services – Business Card</title>
<link href="https://fonts.googleapis.com/css2?family=Poppins:wght@400;600&display=swap" rel="stylesheet">
<style>
  :root {
    --backdrop: #2a2a2c;
    --card: #1f1f21;
    --card-edge: #141415;
    --ink: #ffffff;
    --rule: #5a5a5e;
    --pattern-a: #2b2b2e;
    --pattern-b: #161617;
  }
  * { margin: 0; padding: 0; box-sizing: border-box; }
  html, body { width: 1200px; height: 1108px; overflow: hidden; }
  body {
    background: var(--backdrop);
    font-family: "Poppins", sans-serif;
    color: var(--ink);
    position: relative;
  }
  .card {
    position: absolute;
    top: 194px;
    width: 440px;
    height: 720px;
    border-radius: 26px;
    background: var(--card);
    box-shadow: 0 18px 40px rgba(0,0,0,.45);
    overflow: hidden;
  }
  .card--front { left: 110px; }
  .card--back { left: 650px; }

  /* Front */
  .brand {
    position: absolute;
    top: 70px; left: 0; right: 0;
    text-align: center;
    font-weight: 600;
    color: var(--ink);
  }
  .brand__mark {
    width: 120px; height: 120px;
    border-radius: 50%;
    background: var(--ink);
    margin: 0 auto 26px;
  }
  .brand__name { font-size: 42px; line-height: 1.05; letter-spacing: 1px; }
  .brand__sub { font-size: 15px; letter-spacing: 3px; margin-top: 10px; }

  .person {
    position: absolute;
    top: 392px; left: 0; right: 0;
    text-align: center;
  }
  .person__name { font-size: 30px; font-weight: 600; letter-spacing: .5px; }
  .person__role { font-size: 22px; font-weight: 400; margin-top: 2px; }

  .icon-row {
    position: absolute;
    top: 482px; left: 50px; right: 50px;
    display: flex; align-items: center; gap: 10px;
  }
  .icon-row__rule { flex: 1; height: 1px; background: var(--rule); }
  .icon-row svg { width: 30px; height: 30px; }

  .contact {
    position: absolute;
    top: 524px; left: 0; right: 0;
    text-align: center;
    font-size: 20px;
    line-height: 1.3;
  }
  .contact__divider {
    width: 300px; height: 1px; background: var(--rule);
    margin: 12px auto;
  }

  /* Back */
  .pattern {
    position: absolute; inset: 0;
    background: linear-gradient(160deg, var(--pattern-a) 0%, var(--pattern-b) 65%, #0e0e0f 100%);
  }
  .back-brand {
    position: absolute;
    top: 400px; left: 0; right: 0;
    text-align: center;
    font-weight: 600;
    font-size: 22px;
    letter-spacing: 1px;
  }
  .back-brand__mark {
    width: 56px; height: 56px;
    border-radius: 50%;
    background: var(--ink);
    margin: 0 auto 12px;
  }
  .tagline {
    position: absolute;
    top: 530px; left: 0; right: 0;
    text-align: center;
    font-size: 21px;
    font-weight: 400;
    line-height: 1.35;
    letter-spacing: .5px;
  }
</style>
</head>
<body>

  <section class="card card--front" aria-label="Card front">
    <div class="brand">
      <div class="brand__mark"></div>
      <div class="brand__name">SILVER HERON</div>
      <div class="brand__sub">CONSTRUCTION SERVICES</div>
    </div>

    <div class="person">
      <div class="person__name">DANIELLE VESK</div>
      <div class="person__role">Founder and CEO</div>
    </div>

    <div class="icon-row">
      <span class="icon-row__rule"></span>
      <svg viewBox="0 0 30 30" aria-label="Phone">
        <rect width="30" height="30" rx="5" fill="#fff"/>
        <path d="M9 8c1-1 3-1 3 0l1 4c0 1-1 1.5-2 2 1 2 3 4 5 5 .5-1 1-2 2-2l4 1c1 0 1 2 0 3-1.5 1.5-4 2-7 0s-6-5-7-8 0-4 1-5z" fill="#1f1f21"/>
      </svg>
      <svg viewBox="0 0 30 30" aria-label="Email">
        <rect width="30" height="30" rx="5" fill="#fff"/>
        <rect x="6" y="9" width="18" height="12" fill="none" stroke="#1f1f21" stroke-width="2"/>
        <path d="M6 9l9 7 9-7" fill="none" stroke="#1f1f21" stroke-width="2"/>
      </svg>
      <svg viewBox="0 0 30 30" aria-label="Website">
        <rect width="30" height="30" rx="5" fill="#fff"/>
        <circle cx="15" cy="15" r="8" fill="none" stroke="#1f1f21" stroke-width="2"/>
        <path d="M7 15h16M15 7c-4 4-4 12 0 16M15 7c4 4 4 12 0 16" fill="none" stroke="#1f1f21" stroke-width="1.5"/>
      </svg>
      <span class="icon-row__rule"></span>
    </div>

    <div class="contact">
      <div>303.782.4190</div>
      <div>dvesk@silverheronconst.example</div>
      <div>www.silverheronconst.example</div>
      <div class="contact__divider"></div>
      <div>4816 Alder Brook Way</div>
      <div>Ste 100 Denver, CO. 80451</div>
    </div>
  </section>

  <section class="card card--back" aria-label="Card back">
    <div class="pattern" role="img" aria-label="Repeating glossy brand pattern across the card"></div>
    <div class="back-brand">
      <div class="back-brand__mark"></div>
      <div class="back-brand__name">SILVER HERON</div>
    </div>
    <div class="tagline">THE ROAD TO SUCCESS IS<br>ALWAYS UNDER CONSTRUCTION</div>
  </section>

</body>
</html>
```